Jewelry webpage design project

Velmora is an Online-shop committed to keep the natural beauty of the flowers as jewelry or accessories for women and kids.

Our products are miniaturized flowers kept in transparent resin and assembled on sterling silver. All jewelry and accessories pieces are handmade.

Target market are women who are used to buy per internet from 25 to 45 years old and men who send surprise presents from 25 to 55.
Velmora focuses on the European market, with Germany and Austria as primary customers.

The design of the webpage will have to express the following principles:
• Not complicated but elegant and trustworthy
• Friendly and easy to surf and use
• Express the slogan “beautiful by nature”
• Has to match or flow with the attached logo (doesn’t have to include the same colors)
• Adjust the design to “create the experience” of picking flowers in a garden or silver garden.

As an extra service we will offer special packaging for presents or special events. This option has to be very distinctive or perceptible. The customer have to be able to select the packaging when performing check out.

We are open to any layout but as a guide of how “friendly to use” it has to be, reference attachments are included ( logo, proposed layouts and jewelry photos).

Ecommerce platform will be osCommerce. Within the design proposals hover actions (e.g at menu, links or images) must be shown. No flash application is intended. Image menus are desirable.

Design proposals should include the following layouts:
Main Page
Category Page
Product Page
Packaging Selection (before Checkout)
Checkout Page

*** As an extra Info on the packaging, it is very important to know that we will offer three different packaging options to choose from: the normal one (no extra charges), the one for special occasions (anniversary, Valentine´s day, etc.) and one for birthday presents, both with extra charges.

Target Market(s)

Target market are women from 25 to 45 years old and men who send surprise presents from 25 to 55.

Industry/Entity Type

Internet

Requirements
Must have
• Design proposals should include the following layouts:
- Main Page
- Category Page
- Product Page
- Packaging Selection (before Checkout)
- Checkout Page

Hover actions and transitions (e.g at menu, links or images) must be shown
Nice to have
• Image menus are desirable.
e.g. http://www.quibrendalweb.net/examples/image-menu-1.html
Should not have
• Adobe Flash proposal

```html
<!DOCTYPE html>
<html lang="en">
<head>
<meta charset="utf-8">
<title>Velmora – Product Categories</title>
<link href="https://fonts.googleapis.com/css2?family=Comfortaa:wght@400;700&family=Arimo:wght@400;700&display=swap" rel="stylesheet">
<style>
:root{
  --plum:#8a1c62;
  --plum-dark:#6e1350;
  --plum-footer:#8e1f68;
  --leaf:#8dbf3c;
  --leaf-dark:#6f9e26;
  --ink:#333;
  --muted:#666;
  --line:#ddd;
  --paper:#fff;
  --mist:#f6f4f6;
}
*{margin:0;padding:0;box-sizing:border-box}
html,body{width:958px;height:1200px;overflow:hidden;background:var(--paper);font-family:"Arimo",Arial,sans-serif;color:var(--ink)}
.page{position:relative;width:958px;height:1200px}
.abs{position:absolute}

.site-header{position:absolute;left:0;top:0;width:958px;height:146px;background:var(--mist);border-top:4px solid var(--plum);border-bottom:1px solid #e4e0e4}
.brand{left:96px;top:62px}
.brand-name{font-family:"Arimo",Arial,sans-serif;font-weight:700;font-size:42px;color:var(--ink);line-height:1}

.utility{right:96px;top:20px;font-size:11.5px;color:#444;display:flex;gap:12px;align-items:center}
.utility .sep{color:#bbb}
.utility .current{color:var(--plum)}
.cart{color:#444}
.cart b{color:var(--leaf-dark);font-weight:400}

.callus{left:462px;top:59px;font-size:17px;color:#444;display:flex;align-items:center;gap:6px;white-space:nowrap}
.callus strong{color:var(--leaf-dark);font-weight:700}
.search{left:732px;top:58px;width:130px;height:21px;border:1px solid #ccc;background:#fff;font-size:11px;color:#999;padding:3px 8px}
.search svg{position:absolute;right:6px;top:4px}

.main-nav{left:461px;top:96px;width:401px;height:28px;border:1px solid #ddd;background:#fff;display:flex;font-size:13px}
.main-nav a{flex:1;text-align:center;line-height:26px;color:#333;text-decoration:none}
.main-nav a.active{background:var(--plum);color:#fff;flex:0 0 66px}

.breadcrumb{left:96px;top:175px;font-size:11px;color:#555}
.breadcrumb span.here{color:var(--plum)}
.select{left:677px;top:172px;width:185px;height:20px;border:1px solid #ccc;background:#f3f3f3;font-size:11px;color:#888;padding:3px 8px}
.select i{position:absolute;right:6px;top:4px;width:10px;height:10px;border-radius:50%;background:#aaa}

.hero{left:96px;top:216px;width:529px;height:277px;background:linear-gradient(110deg,#d9eaf3 0%,#a9cfe4 45%,#7e9cb1 70%,#dbe2e8 100%);border:1px solid #ccc}
.hero-caption{left:30px;top:226px;font-family:"Comfortaa",sans-serif;font-weight:700;font-size:27px;color:#fff;text-shadow:0 0 3px #000,0 0 2px #000;white-space:nowrap}

.categories{left:653px;top:216px;width:209px;height:277px;background:var(--leaf);box-shadow:0 2px 6px rgba(0,0,0,.2)}
.categories h2{font-family:"Comfortaa",sans-serif;font-weight:700;font-size:21px;color:#fff;padding:18px 0 12px 26px;border-bottom:2px solid rgba(255,255,255,.7)}
.categories ul{list-style:none;margin:10px 12px 0}
.categories li{height:30px;line-height:30px;color:#fff;font-size:13px;border-bottom:1px solid rgba(255,255,255,.3);padding-left:14px;display:flex;align-items:center;gap:8px}
.categories li:last-child{border:none}
.categories li.hover{background:var(--leaf-dark)}
.categories li i{width:11px;height:11px;border-radius:50%;background:#fff;position:relative;flex:none}
.categories li i::before,.categories li i::after{content:"";position:absolute;background:var(--leaf);left:2px;top:5px;width:7px;height:1px}
.categories li i::after{left:5px;top:2px;width:1px;height:7px}

.section-title{left:96px;top:530px;font-family:"Comfortaa",sans-serif;font-size:21px;color:#222}
.tile{width:171px;height:107px;border:1px solid #ddd;overflow:hidden}
.tile .shot{position:absolute;inset:0}
.tile .label{position:absolute;left:0;bottom:0;width:100%;height:25px;background:rgba(60,60,60,.6);color:#fff;font-size:11.5px;line-height:25px;padding-left:10px}

.about{left:653px;top:534px;width:209px;height:219px;background:#fff;box-shadow:0 1px 6px rgba(0,0,0,.2);padding:36px 22px 0 22px}
.about h3{font-family:"Comfortaa",sans-serif;font-size:18px;font-weight:400;color:#222;margin-bottom:10px}
.about p{font-size:10.5px;line-height:13px;color:#555}
.btn-more{display:inline-block;margin-top:12px;background:var(--plum);color:#fff;font-size:11px;padding:5px 11px}

.site-footer{left:0;top:858px;width:958px;height:286px;background:radial-gradient(ellipse at 45% 40%,#a2307c 0%,var(--plum-footer) 55%,#7a1658 100%)}
.footer-title{font-family:"Comfortaa",sans-serif;font-weight:700;font-size:16px;color:#fff}
.footer-links{list-style:none;font-size:11px;color:#fff}
.footer-links li{height:30px;display:flex;align-items:center;gap:8px}
.footer-links li::before{content:"";width:3px;height:3px;border-radius:50%;background:#fff}
.social li{display:flex;align-items:center;gap:10px;height:39px;color:#fff;font-size:14px;list-style:none}
.social li i{width:25px;height:25px;background:#3a8fd1;display:block}
.social li i.alt{background:#3b5c9b}
.social li i.pro{background:#1f6f9f}
.newsletter{left:653px;top:955px;width:209px;height:22px;background:#fff;font-size:11px;color:#888;padding:4px 8px}
.newsletter b{position:absolute;right:4px;top:3px;width:16px;height:16px;border-radius:50%;background:var(--plum)}
.newsletter b::after{content:"";position:absolute;left:6px;top:5px;border-left:5px solid #fff;border-top:3px solid transparent;border-bottom:3px solid transparent}
.footer-copy{left:653px;top:1064px;font-size:11px;line-height:14px;color:#fff}

.bottom-bar{left:0;top:1144px;width:958px;height:56px;background:var(--mist);border-top:1px solid #e2dde2}
.bottom-copy{left:96px;top:1164px;font-size:11px;color:var(--plum)}
.payments{right:96px;top:1160px;display:flex;align-items:center;gap:4px;font-size:11px;color:var(--plum)}
.payments span{margin-right:6px}
.payments i{width:22px;height:15px;border-radius:2px;display:block;background:#2f7fc2}
.payments i.c1{background:#e0a23a}
.payments i.c2{background:#4a9bd3}
.payments i.c3{background:#5ba5d6}
</style>
</head>
<body>
<div class="page">

  <header class="site-header">
    <div class="abs brand">
      <div class="brand-name">Velmora</div>
    </div>

    <nav class="abs utility">
      <span>My Checkout</span><span class="sep">|</span>
      <span class="current">Login</span><span class="sep">|</span>
      <span>Register</span><span class="sep">|</span>
      <span class="cart">Cart : <b>00</b></span>
    </nav>

    <div class="abs callus">
      <svg width="18" height="14" viewBox="0 0 18 14"><path d="M1 5 Q9 -2 17 5 L14 7 L12 4 Q9 3 6 4 L4 7 Z" fill="var(--leaf-dark)"/><rect x="4" y="7" width="10" height="6" rx="1" fill="var(--leaf-dark)"/></svg>
      <strong>Call Us :</strong> 91+022- 4716 2890
    </div>

    <div class="abs search">Search
      <svg width="11" height="11" viewBox="0 0 11 11"><circle cx="4.5" cy="4.5" r="3.5" fill="none" stroke="#aaa" stroke-width="1.5"/><line x1="7" y1="7" x2="10.5" y2="10.5" stroke="#aaa" stroke-width="1.5"/></svg>
    </div>

    <nav class="abs main-nav">
      <a class="active">Home</a><a>About</a><a>Services</a><a>Products</a><a>Specials</a><a>Contact</a>
    </nav>
  </header>

  <div class="abs breadcrumb">Home &nbsp;&nbsp;&gt;&nbsp;&nbsp; <span class="here">Product Categories</span></div>
  <div class="abs select">Select One<i></i></div>

  <section class="abs hero" role="img" aria-label="Resin flower pendants, rings and a silver necklace beside a woman in a dark dress by a harbour">
    <div class="abs hero-caption">Automatic Photo Transition</div>
  </section>

  <aside class="abs categories">
    <h2>Categories</h2>
    <ul>
      <li><i></i>Bracelets</li>
      <li class="hover"><i></i>Gift Packaging</li>
      <li><i></i>Seasonal</li>
      <li><i></i>Sets</li>
      <li><i></i>Pendant</li>
      <li><i></i>Accesories</li>
    </ul>
  </aside>

  <h2 class="abs section-title">Browse Categories</h2>

  <div class="abs tile" style="left:96px;top:569px"><div class="shot" role="img" aria-label="Blue resin pendant" style="background:linear-gradient(135deg,#b7a98d,#3b3a8a 50%,#8a7d66)"></div><div class="label">Sunflower</div></div>
  <div class="abs tile" style="left:274px;top:569px"><div class="shot" role="img" aria-label="Gold ring with blue stone" style="background:linear-gradient(135deg,#e6e8ea,#c9a43a 45%,#2d3a7a 60%,#d8dde0)"></div><div class="label">Flower B</div></div>
  <div class="abs tile" style="left:452px;top:569px"><div class="shot" role="img" aria-label="Resin disc with yellow flower" style="background:radial-gradient(circle at 40% 45%,#f3c21a 0%,#c8761a 30%,#5a5a5a 55%,#eee 80%)"></div><div class="label">Flower C</div></div>
  <div class="abs tile" style="left:96px;top:699px"><div class="shot" role="img" aria-label="Ring set with pink stones" style="background:linear-gradient(135deg,#fff,#e0478a 40%,#d9a07a 70%,#fff)"></div><div class="label">Edelberry</div></div>
  <div class="abs tile" style="left:274px;top:699px"><div class="shot" role="img" aria-label="Round pendant with pink petals on a cord" style="background:radial-gradient(circle at 55% 55%,#d58a8a 0%,#7a4a5a 35%,#3a3a6a 60%,#fff 85%)"></div><div class="label">Roses &amp; Bouquets</div></div>
  <div class="abs tile" style="left:452px;top:699px"><div class="shot" role="img" aria-label="Resin piece with red orchid" style="background:radial-gradient(circle at 50% 50%,#b23048 0%,#d5c7b4 45%,#8a7a68 90%)"></div><div class="label">Rose Special</div></div>

  <aside class="abs about">
    <h3>A Little About Us</h3>
    <p>Lorem ipsum dolor sit amet, consectetur adipiscing elit. Morbi ac varius elit. Vivamus ut eros risus. Cum sociis natoque penatibus et magnis dis parturient montes, nascetur ridiculus mus. Vivamus elit elit, tristique eu sagittis</p>
    <span class="btn-more">Learn More...</span>
  </aside>

  <footer class="abs site-footer"></footer>
  <h4 class="abs footer-title" style="left:96px;top:925px">Browse Velmora</h4>
  <ul class="abs footer-links" style="left:96px;top:958px">
    <li>Home</li><li>About Us</li><li>Our Product</li><li>Contacts Us</li>
  </ul>

  <h4 class="abs footer-title" style="left:408px;top:925px">Velmora Social</h4>
  <ul class="abs social" style="left:410px;top:957px">
    <li><i></i>FOLLOW US</li>
    <li><i class="alt"></i>BECOME FAN</li>
    <li><i class="pro"></i>JOIN US</li>
  </ul>

  <h4 class="abs footer-title" style="left:653px;top:925px">Newsletter Subscribe</h4>
  <div class="abs newsletter">Email Address<b></b></div>
  <div class="abs footer-copy">All Right Reserved Copyright © 2012<br>Privacy Policy &nbsp;|&nbsp; Terms of Use</div>

  <div class="abs bottom-bar"></div>
  <div class="abs bottom-copy">All Right Reserved Copyright © 2012 | Privacy Policy &nbsp;|&nbsp; Terms of Use</div>
  <div class="abs payments"><span>Payment Options</span><i class="c1"></i><i></i><i class="c2"></i><i class="c3"></i></div>

</div>
</body>
</html>
```